Mother's Day Sale Banner Ad For Jewelry Site

We are looking for a designer to design a banner on our website advertising our Mother's Day Sale. I have enclosed a few pieces of jewelry we would like used in the ad. The ad size needs to be 1187 × 400. The ad should say:

Mother's Day Sale - Save 15% with Promo Code: LOVEMOM

Industry/Entity Type

Jewelry

```html
<!DOCTYPE html>
<html lang="en">
<head>
<meta charset="UTF-8">
<title>Mother's Day Sale Banner</title>
<link rel="stylesheet" href="https://fonts.googleapis.com/css2?family=Allura&family=Great+Vibes&family=Oswald:wght@500&display=swap">
<style>
  :root {
    --navy-deep: #0a0e16;
    --navy-mid: #142640;
    --navy-base: #1f3c68;
    --gold: #eab81e;
    --gold-light: #f3d26a;
    --gold-dark: #a9780f;
    --silver: #d9dde3;
    --white: #ffffff;
  }
  html, body {
    margin: 0;
    padding: 0;
    width: 1200px;
    height: 404px;
    overflow: hidden;
    background: var(--navy-base);
  }
  .banner {
    position: relative;
    width: 1200px;
    height: 404px;
    overflow: hidden;
    background: linear-gradient(180deg, var(--navy-deep) 0%, var(--navy-mid) 38%, var(--navy-base) 72%, #1d3a66 100%);
  }
  .damask-pattern {
    position: absolute;
    left: 0;
    top: 0;
    width: 1200px;
    height: 230px;
    background: linear-gradient(180deg, rgba(40, 44, 56, 0.55) 0%, rgba(30, 40, 60, 0.25) 60%, rgba(31, 60, 104, 0) 100%);
  }
  .headline {
    position: absolute;
    left: 186px;
    top: 128px;
    margin: 0;
    font-family: "Allura", cursive;
    font-weight: 400;
    font-size: 66px;
    line-height: 1;
    color: var(--gold);
    letter-spacing: 1px;
    white-space: nowrap;
  }
  .offer {
    position: absolute;
    left: 362px;
    top: 202px;
    margin: 0;
    font-family: "Great Vibes", cursive;
    font-weight: 400;
    font-size: 84px;
    line-height: 1;
    color: var(--gold);
    -webkit-text-stroke: 1.2px var(--gold);
    white-space: nowrap;
  }
  .promo-code {
    position: absolute;
    left: 479px;
    top: 295px;
    width: 212px;
    height: 35px;
    box-sizing: border-box;
    border: 1.5px solid var(--white);
    display: flex;
    align-items: center;
    justify-content: center;
    font-family: "Oswald", sans-serif;
    font-weight: 500;
    font-size: 19px;
    letter-spacing: 0.3px;
    color: var(--white);
    white-space: nowrap;
  }
  .jewelry-photo {
    position: absolute;
    left: 745px;
    top: 118px;
    width: 405px;
    height: 248px;
    border-radius: 48% 44% 40% 46%;
    background: radial-gradient(ellipse at 35% 45%, var(--gold-light) 0%, var(--gold) 40%, var(--gold-dark) 85%, rgba(169, 120, 15, 0) 100%);
  }
</style>
</head>
<body>
  <section class="banner">
    <div class="damask-pattern" role="img" aria-label="Dark damask scroll pattern fading into navy"></div>
    <h1 class="headline">Mother's Day Sale</h1>
    <p class="offer">Save 15%</p>
    <div class="promo-code">PROMO CODE: LOVEMOM</div>
    <div class="jewelry-photo" role="img" aria-label="Pair of gold rope-twist earrings with diamond-set crossed bands"></div>
  </section>
</body>
</html>
```